College Admissions Consulting needs a small street facing sign for new office location.

I need a graphic design to be used inside window for a banner/sign in office location on a high walking traffic city street, for my company, Campus Lantern. I work with high school students and families on the college planning and selection application process. Please check out the website to learn more about what I do (www.mycampuslantern.example). The banner will be used to market our services at our office location. The final design should utilize logo colors, phone number, and website/email information. I'd like to incorporate a my picture in someway because of face recognition. To be printed on a posterboard or vinyl banner.

Target Market(s)

Parents of high school aged children.

Industry/Entity Type

Education

Font styles to use
Sans Serif

Colors
abd037

Requirements
Must have
• Clean, attractive, and professional design. Attract the attention of people walking by. Information must be clear and readable (phone/email, etc.).
Nice to have
• Utilize the picture with crossed arms (without the brown background on picture).
Emphasize tagline:
Mastering The College Admission Process
....with personalized, professional guidance in planning, selecting, and applying to the right colleges.

```html
<!DOCTYPE html>
<html lang="en">
<head>
<meta charset="utf-8">
<title>Campus Lantern – Office Banner</title>
<link href="https://fonts.googleapis.com/css2?family=PT+Sans:wght@400;700&family=Open+Sans:ital,wght@1,600&display=swap" rel="stylesheet">
<style>
  :root {
    --brand-green: #abd037;
    --deep-green: #7cbc2a;
    --ink: #2b2b2b;
    --logo-grey: #4a4a4a;
    --paper: #ffffff;
    --backdrop: #e6e6e6;
  }
  * { box-sizing: border-box; margin: 0; padding: 0; }
  html, body { width: 1200px; height: 1026px; overflow: hidden; background: var(--backdrop); }
  .banner {
    position: absolute; left: 20px; top: 103px;
    width: 1160px; height: 820px;
    background: var(--paper); overflow: hidden;
    font-family: "PT Sans", sans-serif;
    box-shadow: 0 6px 18px rgba(0,0,0,.25);
  }
  .wave { position: absolute; inset: 0; }
  .brand { position: absolute; left: 72px; top: 48px; display: flex; align-items: center; gap: 14px; }
  .brand-dot { width: 52px; height: 52px; border-radius: 50%; background: var(--brand-green); }
  .brand-name { font-size: 44px; font-weight: 400; color: var(--logo-grey); line-height: 1; }
  .brand-tagline { font-size: 11px; color: var(--logo-grey); letter-spacing: .5px; margin-top: 4px; text-transform: uppercase; }
  .headline {
    position: absolute; left: 72px; top: 178px;
    font-size: 56px; font-weight: 700; line-height: 1.02;
    color: var(--deep-green); text-transform: uppercase; letter-spacing: -.5px;
  }
  .subline {
    position: absolute; left: 72px; top: 300px; width: 720px;
    font-family: "Open Sans", sans-serif; font-style: italic; font-weight: 600;
    font-size: 25px; line-height: 1.3; color: var(--ink);
  }
  .photo { position: absolute; border: 5px solid var(--paper); }
  .photo-graduation { left: 72px; top: 385px; width: 265px; height: 185px;
    background: linear-gradient(135deg, #8a6d52, #2d2d33 55%, #b49a80); }
  .photo-students { left: 80px; top: 590px; width: 265px; height: 190px;
    background: linear-gradient(120deg, #6b4a3a, #3a5fa8 45%, #8a5b44 70%, #9bc94a); }
  .talk-bubble {
    position: absolute; left: 665px; top: -20px; width: 225px; height: 225px;
    background: var(--brand-green); border-radius: 50% 0 50% 50%;
    display: flex; align-items: flex-end; justify-content: center; padding-bottom: 88px;
    color: var(--paper); font-size: 44px; font-weight: 700;
  }
  .portrait {
    position: absolute; left: 760px; top: 0; width: 400px; height: 820px;
    background: linear-gradient(180deg, #2a2220 0%, #1b1b1b 40%, #121212 100%);
  }
  .contacts { position: absolute; left: 375px; top: 580px; list-style: none; }
  .contacts li { display: flex; align-items: center; gap: 14px; height: 57px;
    color: var(--paper); font-size: 30px; font-weight: 700; }
  .contacts svg { width: 38px; height: 38px; flex: none; }
  .social-square { width: 36px; height: 36px; background: var(--paper); flex: none; }
</style>
</head>
<body>
<main class="banner">
  <svg class="wave" viewBox="0 0 1160 820" aria-hidden="true">
    <path d="M0,470 C90,600 260,600 380,540 C500,470 600,395 720,405 C840,415 960,520 1160,520 L1160,820 L0,820 Z" fill="#7cbc2a"/>
    <path d="M0,500 C90,620 260,625 380,570 C500,500 600,430 720,440 C840,450 960,555 1160,545 L1160,820 L0,820 Z" fill="#abd037"/>
  </svg>

  <div class="brand">
    <span class="brand-dot"></span>
    <div>
      <div class="brand-name">Campus Lantern</div>
      <div class="brand-tagline">Mastering the college admission process</div>
    </div>
  </div>

  <h1 class="headline">Mastering the college<br>admisson process</h1>
  <p class="subline">....with personalized, professional guidance in planning, selecting, and applying to the right colleges.</p>

  <div class="photo photo-graduation" role="img" aria-label="Photo of a smiling graduate in cap and gown with his parents"></div>
  <div class="photo photo-students" role="img" aria-label="Photo of a group of smiling high school students holding folders"></div>

  <div class="portrait" role="img" aria-label="Portrait of the consultant smiling with arms crossed, wearing a black top"></div>
  <div class="talk-bubble">Let’s Talk!</div>

  <ul class="contacts">
    <li>
      <svg viewBox="0 0 40 40"><circle cx="20" cy="20" r="19" fill="#fff"/><path d="M13 10c2-1 3 0 4 3l1 3c0 1-1 2-2 3 1 3 3 5 6 6 1-1 2-2 3-2l3 1c3 1 4 2 3 4-1 2-3 3-5 3-9-1-15-7-16-16 0-2 1-4 3-5z" fill="#abd037"/></svg>
      555-014-GRAD(4723)
    </li>
    <li><span class="social-square"></span>mycampuslantern</li>
    <li>
      <svg viewBox="0 0 40 40"><circle cx="20" cy="20" r="17" fill="none" stroke="#fff" stroke-width="3"/><circle cx="20" cy="20" r="6" fill="none" stroke="#fff" stroke-width="3"/></svg>
      hello@mycampuslantern.example
    </li>
    <li>
      <svg viewBox="0 0 40 40" fill="none" stroke="#fff" stroke-width="2.5"><circle cx="20" cy="20" r="17"/><ellipse cx="20" cy="20" rx="7" ry="17"/><path d="M3 20h34M6 11h28M6 29h28"/></svg>
      www.mycampuslantern.example
    </li>
  </ul>
</main>
</body>
</html>
```